Marta Business Card

My wife is going to start her own business with renting holiday appartments to tourists. She needs a design for a new business card... and a new web site.
Look at Stayvolt "Erholung auf dem Lindenwäldchen"

Target Market(s)

Give business card to prospects at any situation

Contact Information for Business Card

not sure what this means

Font styles to use
Script

Colors
fec41a
fee18a

Requirements
Must have
• My wife's handwriting is difficult to read:
Entspannen - Loslassen - Auftanken
Marta & das Lindenwäldchen
Urlaub an einem besonderen Ort
Marta Brecke
Grauer Pfad 7
18471 Alt Feldow
post@marta-brecke.de
www.lindenwaeldchen.net
Nice to have
• Beige background
Font like handwriting

```html
<!DOCTYPE html>
<html lang="de">
<head>
<meta charset="utf-8">
<title>Marta &amp; das Lindenwäldchen – Visitenkarte</title>
<link rel="stylesheet" href="https://fonts.googleapis.com/css2?family=Pinyon+Script&family=Open+Sans:wght@400&display=swap">
<style>
  :root {
    --backdrop: #9a9a9a;
    --paper: #f2f1e4;
    --gold: #fec41a;
    --gold-deep: #c99400;
    --gold-light: #fee18a;
    --ink: #4a4a4a;
    --ink-soft: #555555;
  }
  html, body {
    margin: 0;
    padding: 0;
    width: 1200px;
    height: 1050px;
    overflow: hidden;
    background: var(--backdrop);
  }
  .business-card {
    position: absolute;
    left: 150px;
    top: 245px;
    width: 900px;
    height: 560px;
    box-sizing: border-box;
    background: var(--paper);
    border: 4px solid var(--gold);
    box-shadow: 0 14px 30px rgba(0,0,0,0.25);
    font-family: "Open Sans", Arial, sans-serif;
    color: var(--ink);
  }
  .tagline {
    position: absolute;
    top: 60px;
    left: 0;
    right: 0;
    text-align: center;
    margin: 0;
    font-family: "Pinyon Script", cursive;
    font-weight: 400;
    font-size: 60px;
    color: var(--ink-soft);
  }
  .brand-name {
    position: absolute;
    left: 56px;
    top: 238px;
    margin: 0;
    font-family: "Open Sans", Arial, sans-serif;
    font-weight: 400;
    font-size: 36px;
    line-height: 1.1;
    color: var(--gold-deep);
  }
  .brand-claim {
    position: absolute;
    left: 58px;
    top: 284px;
    margin: 0;
    font-size: 24px;
    line-height: 1.2;
    color: var(--ink-soft);
  }
  .gold-rule {
    position: absolute;
    left: 56px;
    right: 56px;
    top: 330px;
    height: 2px;
    background: linear-gradient(90deg, var(--gold-deep), var(--gold), var(--gold-light), var(--gold));
  }
  .address,
  .contact {
    position: absolute;
    top: 350px;
    margin: 0;
    font-style: normal;
    font-size: 21px;
    line-height: 1.35;
    color: var(--ink-soft);
  }
  .address { left: 58px; }
  .contact { right: 56px; top: 420px; text-align: right; }
</style>
</head>
<body>
  <section class="business-card">
    <h2 class="tagline">Entspannen - Loslassen - Auftanken</h2>
    <h1 class="brand-name">Marta &amp; das Lindenwäldchen</h1>
    <p class="brand-claim">Urlaub an einem besonderen Ort</p>
    <div class="gold-rule"></div>
    <address class="address">
      Grauer Pfad 7<br>
      18471 Alt Feldow<br>
      Germany
    </address>
    <address class="contact">
      +49 160 418 337 52<br>
      post@marta-brecke.de<br>
      lindenwaeldchen.net
    </address>
  </section>
</body>
</html>
```